Lunaform website scandinavian interior design

Existing website: http://lunaform-example.no/

Webdesign for interior designer Ragna Tveitmo. The company name is Lunaform. Scandinavian interiør is known to be simple and elegant. The website will be in Norwegian, we are working on the text. The website needs to have a few more pages than just the front page. Here are the different titles of the pages:

1. Hjem
2. Om Lunaform
3. Tjenester og priser
4.. Kontakt oss

There should be Chatterloop and Pixelane icons somewhere at the bottom of the website.

The logo we want to use is attached (pink with black print, see attachment )

We have attached images for inspiration. We want to use some of these colors. The color in the logo, The style should be elegant, modern and delicate.

It is imprtant that the website is user friendly.

Target Market(s)

People who want to decorate their home
Companies and public sector who need to redecorate

Industry/Entity Type

Interior Designer

Coding

Coded - Design and coding required

Number of Pages Required

5+ page

Font styles to use
Other font styles liked:
• see example in the logo breakdown

Requirements
Must have
• Elegant, modern and delicate design
Images of design, see examples attached
Colors similar to the pictures
Should not have
• Too bright colors
Pictures of people

```html
<!DOCTYPE html>
<html lang="en">
<head>
<meta charset="utf-8">
<title>Lunaform – Farge &amp; Interiørdesign</title>
<link rel="stylesheet" href="https://fonts.googleapis.com/css2?family=Cormorant+Garamond:ital,wght@0,400;0,500;0,600;1,400;1,500&family=EB+Garamond:wght@400;500;600&display=swap">
<style>
  :root {
    --blush: #f3dcd5;
    --blush-soft: #f7e8e3;
    --blush-line: #e7bfb4;
    --ink: #2b1a1d;
    --plum-dark: #261417;
    --plum-deeper: #1d0f11;
    --text: #3d3235;
    --muted: #7a6d70;
    --white: #ffffff;
    --hero-a: #efe9e8;
    --hero-b: #d9cfcd;
  }
  * { margin: 0; padding: 0; box-sizing: border-box; }
  html, body { width: 1200px; height: 4024px; overflow: hidden; }
  body {
    position: relative;
    background: var(--white);
    color: var(--text);
    font-family: "EB Garamond", Georgia, serif;
  }
  .abs { position: absolute; }

  /* Hero */
  .hero {
    left: 0; top: 0; width: 1200px; height: 820px;
    background: linear-gradient(135deg, var(--hero-a) 0%, #f4efee 45%, var(--hero-b) 100%);
    clip-path: polygon(0 0, 100% 0, 100% 740px, 50% 820px, 0 740px);
  }
  .hero-edge { left: 0; top: 740px; width: 1200px; height: 100px; }
  .brand-box {
    left: 120px; top: 0; width: 260px; height: 220px;
    background: var(--blush);
    display: flex; flex-direction: column; align-items: center; justify-content: center;
  }
  .brand-name {
    font-family: "Cormorant Garamond", Georgia, serif;
    font-style: italic; font-weight: 500;
    font-size: 58px; color: var(--ink); line-height: 1;
  }
  .brand-tag {
    margin-top: 14px;
    font-size: 13px; letter-spacing: 3px; color: var(--ink);
  }
  .main-nav {
    left: 420px; top: 52px; width: 680px; height: 30px;
    display: flex; align-items: center; gap: 38px;
    font-size: 15px; letter-spacing: 1.5px; color: var(--ink);
  }
  .main-nav a { color: inherit; text-decoration: none; }
  .main-nav a.active { border-bottom: 1px solid var(--ink); }
  .nav-social { margin-left: auto; display: flex; gap: 14px; font-size: 13px; letter-spacing: 0.5px; }
  .nav-rule { left: 400px; top: 120px; width: 720px; height: 1px; background: #cfc4c2; }
  .hero-title {
    left: 740px; top: 230px;
    font-family: "Cormorant Garamond", Georgia, serif;
    font-style: italic; font-weight: 500; font-size: 96px; color: var(--ink); line-height: 1;
  }
  .hero-sub { left: 740px; top: 348px; font-size: 22px; letter-spacing: 3px; color: var(--ink); }
  .hero-arrows { left: 946px; top: 432px; display: flex; gap: 8px; }
  .arrow-btn {
    width: 52px; height: 52px; display: flex; align-items: center; justify-content: center;
  }
  .arrow-btn.dark { background: #8f8a8a; }
  .arrow-btn.light { background: rgba(255,255,255,0.7); }

  /* Section headings */
  .section-title {
    left: 0; width: 1200px; text-align: center;
    font-family: "Cormorant Garamond", Georgia, serif;
    font-style: italic; font-weight: 500; font-size: 68px; color: var(--ink); line-height: 1;
  }
  .title-rule { left: 520px; width: 160px; height: 1px; background: var(--ink); }

  /* About */
  .about-back { left: 112px; top: 1020px; width: 448px; height: 520px; background: var(--blush); }
  .about-photo {
    left: 144px; top: 1048px; width: 416px; height: 480px;
    background: linear-gradient(160deg, #ece6e2 0%, #c9b6ae 55%, #9a6a6c 100%);
  }
  .about-text { left: 592px; top: 1056px; width: 480px; }
  .about-text h2 {
    font-family: "Cormorant Garamond", Georgia, serif;
    font-weight: 500; font-size: 34px; line-height: 1.2; color: var(--ink); margin-bottom: 26px;
  }
  .about-text p { font-size: 15px; line-height: 1.7; color: var(--text); margin-bottom: 18px; }
  .btn {
    display: inline-block; background: var(--ink); color: var(--white);
    font-size: 13px; letter-spacing: 2px; padding: 11px 20px; text-decoration: none;
  }
  .about-btn { left: 592px; top: 1448px; }

  /* Services */
  .card {
    top: 1820px; width: 304px; height: 628px;
    border: 2px solid var(--blush-line); background: var(--white);
  }
  .card-photo { margin: 12px; height: 288px; }
  .card-photo.kitchen { background: linear-gradient(160deg, #f3f1ef 0%, #c8bfb7 55%, #283456 100%); }
  .card-photo.office { background: linear-gradient(160deg, #e9dfd0 0%, #b89a76 55%, #6f5a45 100%); }
  .card-photo.lounge { background: linear-gradient(160deg, #eef0f2 0%, #c9ced3 55%, #6c6e72 100%); }
  .card-body { padding: 24px 28px 0; }
  .card-body h3 {
    font-family: "EB Garamond", Georgia, serif; font-weight: 600;
    font-size: 28px; letter-spacing: 2px; line-height: 1.15; color: var(--ink); margin-bottom: 16px;
  }
  .card-body p { font-size: 14px; line-height: 1.6; color: var(--text); margin-bottom: 26px; }

  /* Testimonial */
  .testi-panel { left: 112px; top: 2832px; width: 488px; height: 528px; background: var(--blush); }
  .testi-photo {
    left: 600px; top: 2832px; width: 488px; height: 528px;
    background: linear-gradient(170deg, #e4e2df 0%, #f2f1ef 50%, #c9c5c0 100%);
  }
  .avatar {
    left: 160px; top: 2872px; width: 120px; height: 120px; border-radius: 50%;
    background: linear-gradient(160deg, #7b5a52, #3a2a27); border: 4px solid var(--white);
  }
  .testi-name { left: 300px; top: 2900px; font-size: 22px; color: var(--ink); }
  .testi-role { left: 300px; top: 2934px; font-size: 15px; color: var(--muted); }
  .quote-mark {
    left: 440px; top: 2860px;
    font-family: "Cormorant Garamond", Georgia, serif; font-size: 110px; line-height: 1; color: #c9a49a;
  }
  .testi-vertical {
    left: 548px; top: 2890px; height: 260px;
    writing-mode: vertical-rl; font-size: 18px; letter-spacing: 6px; color: var(--ink);
  }
  .testi-quote { left: 160px; top: 3040px; width: 370px; font-size: 17px; line-height: 1.7; color: var(--text); }
  .testi-arrows { left: 112px; top: 3292px; display: flex; }
  .testi-arrows .arrow-btn { width: 60px; height: 60px; }
  .testi-arrows .dark { background: #a79d9b; }
  .testi-arrows .light { background: #ddd2cf; }

  /* Newsletter */
  .newsletter { left: 0; top: 3432px; width: 1200px; height: 188px; background: var(--blush); }
  .news-title {
    left: 192px; top: 3496px;
    font-family: "EB Garamond", Georgia, serif; font-weight: 500; font-size: 36px; color: var(--ink);
  }
  .news-input {
    left: 560px; top: 3496px; width: 440px; height: 50px;
    background: var(--blush-soft); border-bottom: 1px solid #c9a49a;
    display: flex; align-items: center; justify-content: space-between; padding: 0 18px;
    font-size: 16px; color: var(--muted);
  }

  /* Footer */
  .footer { left: 0; top: 3620px; width: 1200px; height: 340px; background: var(--plum-dark); color: #e9dcd8; }
  .foot-col h4 { font-family: "EB Garamond", Georgia, serif; font-weight: 500; font-size: 24px; margin-bottom: 22px; color: var(--white); }
  .foot-col li { list-style: none; font-size: 16px; line-height: 1.5; margin-bottom: 12px; display: flex; gap: 14px; align-items: flex-start; }
  .quick-links { left: 128px; top: 3664px; }
  .contact-details { left: 448px; top: 3664px; }
  .foot-brand {
    left: 800px; top: 3648px; width: 272px; height: 232px; background: var(--blush);
    display: flex; flex-direction: column; align-items: center; justify-content: center;
  }
  .foot-social { left: 800px; top: 3920px; width: 272px; display: flex; justify-content: center; gap: 16px; font-size: 13px; color: #e9dcd8; }
  .bottom-bar {
    left: 0; top: 3960px; width: 1200px; height: 64px; background: var(--plum-deeper);
    display: flex; align-items: center; padding-left: 128px; font-size: 15px; color: #d9cbc7;
  }
</style>
</head>
<body>

<header>
  <div class="abs hero" role="img" aria-label="Bright living room with a pink armchair, a round side table and a vase with bare branches"></div>
  <svg class="abs hero-edge" width="1200" height="100" viewBox="0 0 1200 100" aria-hidden="true">
    <polyline points="0,16 600,96 1200,16" fill="none" stroke="#d4b1a8" stroke-width="1.5"/>
  </svg>

  <div class="abs brand-box">
    <span class="brand-name">Lunaform</span>
    <span class="brand-tag">FARGE &amp; INTERIØRDESIGN</span>
  </div>

  <nav class="abs main-nav">
    <a class="active" href="#">HOME</a>
    <a href="#">ABOUT LUNAFORM</a>
    <a href="#">SERVICES AND PRICES</a>
    <a href="#">CONTACT US</a>
    <span class="nav-social"><span>Chatterloop</span><span>Chirpwell</span><span>Pixelane</span></span>
  </nav>
  <div class="abs nav-rule"></div>

  <div class="abs hero-title">Lunaform</div>
  <div class="abs hero-sub">FARGE &amp; INTERIORDESIGN</div>
  <div class="abs hero-arrows">
    <span class="arrow-btn dark"><svg width="16" height="16" viewBox="0 0 16 16"><path d="M10 3 L5 8 L10 13" fill="none" stroke="#fff" stroke-width="2"/></svg></span>
    <span class="arrow-btn light"><svg width="16" height="16" viewBox="0 0 16 16"><path d="M6 3 L11 8 L6 13" fill="none" stroke="#2b1a1d" stroke-width="2"/></svg></span>
  </div>
</header>

<main>
  <section class="welcome">
    <h1 class="abs section-title" style="top:880px;">Welcome to Lunaform</h1>
    <div class="abs title-rule" style="top:956px;"></div>

    <div class="abs about-back"></div>
    <div class="abs about-photo" role="img" aria-label="Dining room with pendant lamps, a long wooden table and a pink bench under an arched window"></div>
    <div class="abs about-text">
      <h2>Need help developing interior environments?</h2>
      <p>Lunaform AS works on the development of interior environments for private homes, companies and the public sector. To find the best solution for a project, whether it is a room or more, requires knowledge and feeling for the details. Using professional expertise in the field we help you both now and later.</p>
      <p>Using floor plans, furniture plans, 3D drawings, colour maps or "make a mood collage", we find the best solution for you and your space.</p>
      <p>The goal is always to focus on the customer – get what you want.</p>
    </div>
    <a class="abs btn about-btn" href="#">READ MORE</a>
  </section>

  <section class="services">
    <h2 class="abs section-title" style="top:1684px;">Services</h2>
    <div class="abs title-rule" style="top:1756px;"></div>

    <article class="abs card" style="left:112px;">
      <div class="card-photo kitchen" role="img" aria-label="White kitchen with a navy island and brass pendant lights"></div>
      <div class="card-body">
        <h3>PRIVATE<br>INTERIOR</h3>
        <p>Calm and personal homes, planned room by room with colour, light and furniture that suit the way you live.</p>
        <a class="btn" href="#">READ MORE</a>
      </div>
    </article>

    <article class="abs card" style="left:448px;">
      <div class="card-photo office" role="img" aria-label="Office with wooden slat ceiling and rows of work desks"></div>
      <div class="card-body">
        <h3>CORPORATE<br>INTERIOR</h3>
        <p>Offices and shared spaces that work well every day, with good flow, clear zones and a warm, simple finish.</p>
        <a class="btn" href="#">READ MORE</a>
      </div>
    </article>

    <article class="abs card" style="left:780px;">
      <div class="card-photo lounge" role="img" aria-label="Open lounge area with grey sofas and white tables"></div>
      <div class="card-body">
        <h3>PUBLIC<br>INTERIOR</h3>
        <p>Schools, clinics and public rooms made welcoming and durable, planned to serve many people over time.</p>
        <a class="btn" href="#">READ MORE</a>
      </div>
    </article>
  </section>

  <section class="testimonials">
    <h2 class="abs section-title" style="top:2636px;">Testimonials</h2>
    <div class="abs title-rule" style="top:2708px;"></div>

    <div class="abs testi-panel"></div>
    <div class="abs avatar" role="img" aria-label="Portrait of the client"></div>
    <div class="abs testi-name">Selma Brekk</div>
    <div class="abs testi-role">Private client</div>
    <div class="abs quote-mark">“ “</div>
    <div class="abs testi-vertical">- Testimonials -</div>
    <p class="abs testi-quote">Lunaform helped us turn a dark, crowded flat into a light and calm home. Every choice of colour and furniture felt right, and the whole process was easy and friendly from start to finish.</p>
    <div class="abs testi-arrows">
      <span class="arrow-btn dark"><svg width="16" height="16" viewBox="0 0 16 16"><path d="M10 3 L5 8 L10 13" fill="none" stroke="#fff" stroke-width="2"/></svg></span>
      <span class="arrow-btn light"><svg width="16" height="16" viewBox="0 0 16 16"><path d="M6 3 L11 8 L6 13" fill="none" stroke="#2b1a1d" stroke-width="2"/></svg></span>
    </div>
    <div class="abs testi-photo" role="img" aria-label="Dining corner with a dark pendant lamp, yellow and white chairs and a ladder shelf"></div>
  </section>

  <section class="abs newsletter"></section>
  <h2 class="abs news-title">Newsletter Subscribe</h2>
  <div class="abs news-input">
    <span>Enter Email id</span>
    <svg width="22" height="22" viewBox="0 0 24 24"><path d="M2 12 L22 3 L15 22 L11 13 Z" fill="#2b1a1d"/></svg>
  </div>
</main>

<footer>
  <div class="abs footer"></div>
  <div class="abs foot-col quick-links">
    <h4>Quick Links</h4>
    <ul>
      <li>›&nbsp; Home</li>
      <li>›&nbsp; About Lunaform</li>
      <li>›&nbsp; Services &amp; Prices</li>
      <li>›&nbsp; Contact Us</li>
    </ul>
  </div>
  <div class="abs foot-col contact-details">
    <h4>Contact Details</h4>
    <ul>
      <li><svg width="16" height="20" viewBox="0 0 16 20"><path d="M8 1 C4 1 1 4 1 8 C1 13 8 19 8 19 C8 19 15 13 15 8 C15 4 12 1 8 1 Z" fill="none" stroke="#e9dcd8" stroke-width="1.5"/><circle cx="8" cy="8" r="2.5" fill="#e9dcd8"/></svg><span>Strandveien 14,<br>0250 Oslo, Norway</span></li>
      <li><svg width="16" height="16" viewBox="0 0 16 16"><path d="M3 1 L6 1 L7 5 L5 6 C6 8 8 10 10 11 L11 9 L15 10 L15 13 C15 14 14 15 13 15 C7 15 1 9 1 3 C1 2 2 1 3 1 Z" fill="#e9dcd8"/></svg><span>+47 900 12 345</span></li>
      <li><svg width="18" height="14" viewBox="0 0 18 14"><rect x="1" y="1" width="16" height="12" fill="none" stroke="#e9dcd8" stroke-width="1.5"/><path d="M1 1 L9 8 L17 1" fill="none" stroke="#e9dcd8" stroke-width="1.5"/></svg><span>post@lunaform-example.no</span></li>
    </ul>
  </div>
  <div class="abs foot-brand">
    <span class="brand-name">Lunaform</span>
    <span class="brand-tag">FARGE &amp; INTERIØRDESIGN</span>
  </div>
  <div class="abs foot-social"><span>Chatterloop</span><span>Chirpwell</span><span>Pixelane</span></div>
  <div class="abs bottom-bar">© 2020 &nbsp;|&nbsp; www.lunaform-example.no</div>
</footer>

</body>
</html>
```